Customs House descriptive business cards

We require a two-sided business card that has a simple yet elegant design. We want to be able to promote our services as a customs house. This card should include our logo, contact info and services offered with the logo being on one side and the contact info and services on the flip side

Target Market(s)

Importers / exporters to and from the Bahamas

Industry/Entity Type

Logistics

Contact Information for Business Card

The front side of the card could have the logo and the flip side should have the other relevant info

Font styles to use
Serif

Colors

Designer to choose colors to be used in the design.

Requirements
Must have
• (Harbourline Agents Ltd) Logo, address and contact info also services:
• import customs clearance, Delivery & HAndling services,Florida pickups, Export packing & Crating Services, export customs clearance, Consulting

```html
<!DOCTYPE html>
<html lang="en">
<head>
<meta charset="utf-8">
<title>Harbourline Agents Ltd — Business Card</title>
<link href="https://fonts.googleapis.com/css2?family=EB+Garamond:wght@400;500&display=swap" rel="stylesheet">
<style>
  :root {
    --backdrop: #3a3a3c;
    --card-dark: #1c1c1e;
    --card-mid: #2b2b2d;
    --brand-blue: #2f8fd6;
    --wave-blue: #1f66b8;
    --wave-light: #2a9ce0;
    --text-light: #f1f1f1;
    --rule: #9a9a9a;
  }
  * { margin: 0; padding: 0; box-sizing: border-box; }
  html, body { width: 1200px; height: 1000px; overflow: hidden; }
  body {
    background: var(--backdrop);
    font-family: "EB Garamond", Garamond, serif;
    position: relative;
  }
  .card {
    position: absolute;
    left: 220px;
    width: 760px;
    height: 434px;
    border-radius: 28px;
    overflow: hidden;
    background: linear-gradient(135deg, var(--card-mid) 0%, var(--card-dark) 55%, var(--card-mid) 100%);
    box-shadow: 0 14px 30px rgba(0,0,0,0.45);
  }
  .card--front { top: 42px; }
  .card--back { top: 524px; }

  /* Front */
  .brand {
    position: absolute;
    inset: 0;
    display: flex;
    flex-direction: column;
    align-items: center;
    justify-content: center;
    gap: 18px;
  }
  .brand__dot {
    width: 26px; height: 26px; border-radius: 50%;
    background: var(--brand-blue);
  }
  .brand__name {
    color: var(--brand-blue);
    font-weight: 500;
    font-size: 40px;
    letter-spacing: 3px;
    text-transform: uppercase;
  }

  /* Back */
  .wave { position: absolute; left: 0; bottom: 0; width: 760px; height: 434px; }
  .services {
    position: absolute;
    right: 432px;
    top: 118px;
    text-align: right;
    color: var(--text-light);
    font-size: 17px;
    line-height: 26px;
  }
  .services__title {
    color: var(--brand-blue);
    font-size: 13px;
    letter-spacing: 1px;
    text-transform: uppercase;
    margin-bottom: 6px;
  }
  .services__list { list-style: none; }
  .services__list li::after {
    content: "";
    display: inline-block;
    width: 7px; height: 7px;
    margin-left: 12px;
    background: var(--wave-light);
    vertical-align: middle;
  }
  .divider {
    position: absolute;
    left: 345px;
    top: 150px;
    width: 1px;
    height: 180px;
    background: var(--rule);
  }
  .contact {
    position: absolute;
    left: 368px;
    top: 150px;
    color: var(--text-light);
    font-size: 17px;
    line-height: 22px;
  }
  .contact__name { color: var(--brand-blue); font-size: 26px; line-height: 28px; }
  .contact__role { font-size: 16px; margin-bottom: 16px; }
  .contact__address { margin-bottom: 14px; }
  .contact__line { display: flex; align-items: center; gap: 8px; }
  .contact__line svg { width: 13px; height: 13px; flex: none; }
  .accent { color: var(--brand-blue); }
</style>
</head>
<body>

<section class="card card--front" aria-label="Card front">
  <div class="brand">
    <span class="brand__dot"></span>
    <span class="brand__name">Harbourline Agents Ltd</span>
  </div>
</section>

<section class="card card--back" aria-label="Card back">
  <svg class="wave" viewBox="0 0 760 434" aria-hidden="true">
    <path d="M0 300 C 120 350, 260 420, 760 395 L760 434 L0 434 Z" fill="var(--wave-blue)"/>
    <path d="M0 282 C 110 320, 220 380, 340 405 C 230 370, 110 322, 0 296 Z" fill="var(--wave-light)"/>
  </svg>

  <div class="services">
    <p class="services__title">Services offered :</p>
    <ul class="services__list">
      <li>Import Customs Clearance</li>
      <li>Delivery &amp; HAndling Services</li>
      <li>Florida Pickups</li>
      <li>Export packing &amp; Crating Services</li>
      <li>Export Customs Clearance</li>
      <li>Consulting</li>
    </ul>
  </div>

  <div class="divider"></div>

  <div class="contact">
    <p class="contact__name">Marcus Whitfield</p>
    <p class="contact__role">President</p>
    <p class="contact__address">1480 Bay Street,<br>Suite 210, Nassau N-4417</p>
    <p class="contact__line">
      <svg viewBox="0 0 16 16"><path d="M3 1h3l1.5 4-2 1.3a9 9 0 0 0 4.2 4.2L11 8.5l4 1.5v3a2 2 0 0 1-2 2A12 12 0 0 1 1 3a2 2 0 0 1 2-2z" fill="var(--text-light)"/></svg>
      242.555.0148
    </p>
    <p class="contact__line">
      <svg viewBox="0 0 16 16"><circle cx="8" cy="8" r="6.5" fill="none" stroke="var(--text-light)" stroke-width="1.5"/><path d="M1.5 8h13M8 1.5c3 3 3 10 0 13M8 1.5c-3 3-3 10 0 13" fill="none" stroke="var(--text-light)" stroke-width="1.2"/></svg>
      marcus@harbourlineagents.com
    </p>
    <p class="contact__line">
      <svg viewBox="0 0 16 16"><rect x="1" y="3" width="14" height="10" rx="1" fill="var(--text-light)"/><path d="M1 4l7 5 7-5" fill="none" stroke="var(--card-dark)" stroke-width="1.4"/></svg>
      <span>www.<span class="accent">harbourlineagents</span>.com</span>
    </p>
  </div>
</section>

</body>
</html>
```